依頼詳細
◆デザインのイメージ
・『営業』『広告』の雰囲気ではなく、一見『ご家庭用の年賀状』の雰囲気
・とにかく可愛い、柔らかくほのぼのとした感じ、愛らしい感じ
『仲の良い友達からの可愛い年賀状だ!と思ったら、ルミエ桜台からだった!』という感じ
・干支もさりげなく登場していると嬉しいです
・一言コメントを書けるスペースが少しあると助かります

ご不明な点がございましたらお気軽にご連絡ください。

よろしくお願いします。

記載項目
◆文字原稿を添付いたします
◆手持ちのプリンターで印刷します
◆納品はPDFまたはJPGなら対応できます
◆店舗名は無くても大丈夫です(宛先面に差出人印刷をしています)
希望イメージ
シンプル 複雑
単色 カラフル
暗い 明るい
日常 高級
遊び心 厳粛
未来的 伝統的
女性的 男性的
希望する色
納品ファイル
• 高解像度JPG (.jpg)
補足説明
サロンHP
https://rumie-salon.example
■ 選んだ理由

好みの要素を全て盛り込んで頂けた作品でした。

■ 提案者全員のお礼・コメント

多くの提案を有難うございます。
いつも当選を1つに絞るのがとても大変です。
また次回もよろしくお願いします。

```html
<!DOCTYPE html>
<html lang="ja">
<head>
<meta charset="utf-8">
<title>年賀状 令和3年</title>
<link rel="stylesheet" href="https://fonts.googleapis.com/css2?family=Noto+Sans+JP:wght@400;500;700;900&family=Noto+Serif+JP:wght@500;700&display=swap">
<style>
  :root {
    --paper: #ffffff;
    --sun-core: #fde3cc;
    --sun-edge: #f39a52;
    --ink: #231815;
    --ink-soft: #4a4a4a;
    --white: #ffffff;
    --accent-red: #d7261e;
    --frame-gold: #c9a86a;
    --eco-green: #3d9a3c;
    --photo-a: #d8b99a;
    --photo-b: #8a6a55;
  }
  * { margin: 0; padding: 0; box-sizing: border-box; }
  html, body { width: 826px; height: 1200px; overflow: hidden; background: var(--paper); }
  body { font-family: "Noto Sans JP", sans-serif; color: var(--ink); }
  .card { position: relative; width: 826px; height: 1200px; background: var(--paper); }

  .sun {
    position: absolute; left: 124px; top: 40px; width: 578px; height: 590px; border-radius: 50%;
    overflow: hidden;
    background: radial-gradient(circle at 50% 45%, var(--sun-core) 0%, #f9c596 45%, var(--sun-edge) 100%);
  }
  .zodiac-photo {
    position: absolute; left: 46px; top: 290px; width: 486px; height: 210px; border-radius: 40px;
    background: radial-gradient(ellipse at 50% 55%, var(--photo-b) 0%, var(--photo-a) 55%, rgba(248,200,150,0) 75%);
  }
  .greeting {
    position: absolute; top: 112px; left: 0; width: 100%; text-align: center;
    color: var(--white); font-weight: 700; font-size: 60px; line-height: 1.02; letter-spacing: 1px;
  }
  .era-date {
    position: absolute; top: 306px; left: 0; width: 100%; text-align: center;
    font-family: "Noto Serif JP", serif; font-size: 24px; font-weight: 500; color: var(--ink);
  }
  .comment-space {
    position: absolute; top: 548px; left: 0; width: 100%; text-align: center;
    color: var(--white); font-size: 26px; font-weight: 500; letter-spacing: 1px; line-height: 1.3;
  }
  .message {
    position: absolute; top: 640px; left: 0; width: 100%; text-align: center;
    font-size: 31px; font-weight: 700;
  }
  .opening {
    position: absolute; top: 688px; left: 0; width: 100%; text-align: center;
    font-size: 24px; font-weight: 700;
  }
  .voucher { position: absolute; left: 273px; top: 780px; width: 280px; height: 92px; }
  .voucher-label {
    position: absolute; top: 806px; left: 0; width: 100%; text-align: center;
    font-size: 26px; font-weight: 700;
  }
  .offer-title {
    position: absolute; top: 912px; left: 0; width: 100%; text-align: center;
    font-size: 30px; font-weight: 900; letter-spacing: 2px;
  }
  .offer-detail {
    position: absolute; top: 956px; left: 0; width: 100%; text-align: center;
    font-size: 19px; font-weight: 700;
  }
  .offer-scope {
    position: absolute; top: 984px; left: 0; width: 100%; text-align: center;
    font-size: 11px; color: var(--ink-soft);
  }
  .notes {
    position: absolute; top: 1012px; left: 0; width: 100%; text-align: center;
    font-size: 11px; color: var(--ink-soft); letter-spacing: 0.5px;
  }
  .notes .expiry-badge {
    display: inline-block; background: var(--accent-red); color: var(--white);
    padding: 1px 6px; font-weight: 700; margin: 0 6px 0 14px;
  }
  .notes .expiry-date { font-weight: 700; color: var(--ink); margin-right: 14px; }
  .safety {
    position: absolute; left: 220px; top: 1080px; width: 428px; height: 78px;
    border: 2px dashed var(--eco-green); text-align: center; color: var(--eco-green);
    font-size: 17px; font-weight: 700; line-height: 1.5; padding-top: 12px;
  }
</style>
</head>
<body>
<div class="card">
  <div class="sun">
    <div class="zodiac-photo" role="img" aria-label="干支の牛の置物2体の写真"></div>
  </div>
  <div class="greeting">A<br>HAPPY<br>NEW YEAR!</div>
  <div class="era-date">令和３年元旦</div>
  <div class="comment-space">コメントあればここに</div>

  <p class="message">今年もスタッフ一同技術向上に励んで参ります</p>
  <p class="opening">年始は8日(金)より営業いたします</p>

  <svg class="voucher" viewBox="0 0 280 92" aria-hidden="true">
    <rect x="4" y="4" width="272" height="84" rx="40" fill="none" stroke="var(--frame-gold)" stroke-width="2"/>
    <rect x="12" y="12" width="256" height="68" rx="32" fill="none" stroke="var(--frame-gold)" stroke-width="1"/>
  </svg>
  <p class="voucher-label">金券2,000円</p>

  <p class="offer-title">この年賀状ご持参ください！</p>
  <p class="offer-detail">90分以上のコースでお会計より2000円お値引きいたします！</p>
  <p class="offer-scope">(A・B・Cコースも可)</p>

  <p class="notes">
    ※期間中1回ご利用頂けます
    <span class="expiry-badge">有効期限</span><span class="expiry-date">令和3年1月末日</span>
    ※他の割引との併用はできません
  </p>

  <div class="safety">お客様の安心・安全のために、<br>24時間オゾン発生機により空間除菌中です</div>
</div>
</body>
</html>
```